KRV announces Absolutely No Fees!!

Corvalt Swift Lending is financial institution operating in the Caribbean . The company is planning to remove all fees from its loan process . The company will charge its customer absolutely no fees. No application fees, no underwriting fees, no origination fees, no late payment fees, no penalty fees, no credit bureau fees, no transaction fees etc etc etc…absolutely no fees.

The company would like to create an advertising campaign that blows the market away with this information. As no other bank/financial institution has this offer.

Target Market(s)

Mass Market - Caribbean

Industry/Entity Type

Banking / Finance

Requirements
Must have
• Please be creative.

```html
<!DOCTYPE html>
<html lang="en">
<head>
<meta charset="utf-8">
<title>KRV – Absolutely No Fees</title>
<link rel="stylesheet" href="https://fonts.googleapis.com/css2?family=Montserrat:wght@500;600;700;800;900&family=Nunito:wght@800;900&display=swap">
<style>
  :root {
    --stage: #9a9a9a;
    --red-deep: #a9000f;
    --red: #d40d1c;
    --orange: #f57a2e;
    --glow: #ffb347;
    --yellow: #fdd329;
    --white: #ffffff;
    --shadow-red: #6e0008;
    --ink: #4a4a4a;
    --navy: #25314f;
  }
  * { margin: 0; padding: 0; box-sizing: border-box; }
  html, body { width: 967px; height: 1200px; overflow: hidden; }
  body { background: var(--stage); position: relative; font-family: "Montserrat", sans-serif; }

  .poster {
    position: absolute; left: 73px; top: 20px; width: 820px; height: 1160px; overflow: hidden;
    background:
      radial-gradient(ellipse 420px 520px at 50% 60%, var(--glow) 0%, var(--orange) 30%, var(--red) 75%, var(--red-deep) 110%);
  }
  .rays { position: absolute; inset: 0; }

  .eyebrow {
    position: absolute; top: 70px; left: 0; width: 100%;
    display: flex; justify-content: center; align-items: center; gap: 12px;
    color: var(--yellow); font-weight: 800; font-size: 50px; letter-spacing: 9px;
  }
  .eyebrow::before, .eyebrow::after {
    content: ""; width: 100px; height: 2px; background: var(--yellow);
  }
  .eyebrow span { margin-right: -9px; }

  .lead {
    position: absolute; top: 134px; width: 100%; text-align: center;
    color: var(--white); font-weight: 600; font-size: 56px; letter-spacing: 7px;
  }
  .headline {
    position: absolute; top: 188px; width: 100%; text-align: center;
    color: var(--white); font-weight: 900; font-size: 128px; letter-spacing: -3px; line-height: 1.1;
    text-shadow: 4px 4px 0 var(--shadow-red);
  }

  .fee-list {
    position: absolute; top: 336px; left: 80px; width: 680px;
    display: grid; grid-template-columns: 340px 340px; grid-auto-flow: column; grid-template-rows: repeat(3, 43px);
    list-style: none;
  }
  .fee-list li {
    display: flex; align-items: center; gap: 10px;
    color: var(--white); font-family: "Nunito", sans-serif; font-weight: 900; font-size: 23.5px;
  }
  .fee-list svg { width: 26px; height: 26px; flex: none; }

  .photo {
    position: absolute; left: 78px; top: 480px; width: 680px; height: 530px;
    border-radius: 150px 150px 0 0;
    background: linear-gradient(90deg, #c32a3c 0%, #b82636 45%, var(--navy) 55%, #2b3757 100%);
    opacity: 0.9;
  }

  .footer-band { position: absolute; left: 0; top: 0; width: 820px; height: 1160px; }

  .web {
    position: absolute; top: 1020px; left: 58px; width: 356px; text-align: center;
    color: var(--ink); font-weight: 500; font-size: 21px;
  }
  .web b { color: var(--red); font-weight: 700; }

  .call {
    position: absolute; top: 1066px; left: 68px; width: 333px; height: 34px;
    background: var(--red); border-radius: 17px;
    display: flex; align-items: center; gap: 8px; padding-left: 8px;
    color: var(--white); font-weight: 700; font-size: 17.5px;
  }
  .call svg { width: 22px; height: 22px; flex: none; }
  .call em { font-style: normal; color: var(--yellow); }

  .social { position: absolute; top: 1110px; left: 148px; display: flex; gap: 9px; }
  .social span { width: 28px; height: 28px; border: 2px solid var(--ink); border-radius: 50%; }

  .brand {
    position: absolute; top: 1010px; left: 530px; width: 234px; text-align: center;
    color: var(--red); font-weight: 900; font-size: 88px; letter-spacing: 4px; line-height: 110px;
  }
</style>
</head>
<body>
  <main class="poster">
    <svg class="rays" viewBox="0 0 820 1160" aria-hidden="true">
      <g fill="#ffffff" opacity="0.06">
        <polygon points="410,700 -200,0 -100,0"/>
        <polygon points="410,700 60,0 160,0"/>
        <polygon points="410,700 330,0 430,0"/>
        <polygon points="410,700 620,0 720,0"/>
        <polygon points="410,700 900,0 1000,0"/>
        <polygon points="410,700 0,500 0,600"/>
        <polygon points="410,700 820,420 820,520"/>
        <polygon points="410,700 0,900 0,1000"/>
        <polygon points="410,700 820,820 820,920"/>
      </g>
    </svg>

    <div class="eyebrow"><span>WE OFFER</span></div>
    <div class="lead">ABSOLUTELY</div>
    <h1 class="headline">NO FEES!!</h1>

    <ul class="fee-list">
      <li><svg viewBox="0 0 26 26"><circle cx="12" cy="14" r="10" fill="none" stroke="#fff" stroke-width="2"/><path d="M7 14l4 4 10-13" fill="none" stroke="#fdd329" stroke-width="3" stroke-linecap="round"/></svg>No application fees</li>
      <li><svg viewBox="0 0 26 26"><circle cx="12" cy="14" r="10" fill="none" stroke="#fff" stroke-width="2"/><path d="M7 14l4 4 10-13" fill="none" stroke="#fdd329" stroke-width="3" stroke-linecap="round"/></svg>No origination fees</li>
      <li><svg viewBox="0 0 26 26"><circle cx="12" cy="14" r="10" fill="none" stroke="#fff" stroke-width="2"/><path d="M7 14l4 4 10-13" fill="none" stroke="#fdd329" stroke-width="3" stroke-linecap="round"/></svg>No penalty fees</li>
      <li><svg viewBox="0 0 26 26"><circle cx="12" cy="14" r="10" fill="none" stroke="#fff" stroke-width="2"/><path d="M7 14l4 4 10-13" fill="none" stroke="#fdd329" stroke-width="3" stroke-linecap="round"/></svg>No underwriting fees</li>
      <li><svg viewBox="0 0 26 26"><circle cx="12" cy="14" r="10" fill="none" stroke="#fff" stroke-width="2"/><path d="M7 14l4 4 10-13" fill="none" stroke="#fdd329" stroke-width="3" stroke-linecap="round"/></svg>No late payment fees</li>
      <li><svg viewBox="0 0 26 26"><circle cx="12" cy="14" r="10" fill="none" stroke="#fff" stroke-width="2"/><path d="M7 14l4 4 10-13" fill="none" stroke="#fdd329" stroke-width="3" stroke-linecap="round"/></svg>No credit bureau fees</li>
    </ul>

    <div class="photo" role="img" aria-label="Photo of a surprised, delighted woman in a red sweater and a shocked man in a navy shirt, hands raised in excitement"></div>

    <svg class="footer-band" viewBox="0 0 820 1160" aria-hidden="true">
      <polygon points="0,1002 820,888 820,932 0,1010" fill="var(--yellow)"/>
      <polygon points="0,1010 820,932 820,1160 0,1160" fill="var(--white)"/>
    </svg>

    <p class="web">www.<b>corvaltswift</b>.com/tt</p>
    <div class="call">
      <svg viewBox="0 0 22 22"><circle cx="11" cy="11" r="10" fill="#fff"/><path d="M7.5 6.5c.6-.6 1.4-.5 1.8.2l.8 1.5c.3.6.1 1.1-.4 1.5l-.5.4c.5 1.2 1.4 2.1 2.6 2.6l.4-.5c.4-.5 1-.7 1.5-.4l1.5.8c.7.4.8 1.2.2 1.8l-.7.7c-.9.9-3.5.1-5.3-1.7S6.2 8.1 7.1 7.2z" fill="var(--red)"/></svg>
      <span>Call Us Today: <em>8685550142</em></span>
    </div>
    <div class="social" aria-label="Social media links"><span></span><span></span><span></span><span></span></div>

    <div class="brand">KRV</div>
  </main>
</body>
</html>
```